KLV Business Card - Courier/Transportation - Needs Double Sided Business Card

I am searching for business cards for my company. Currently I just need cards for the (3) founders.

We are a new courier/transporation company that specializes in the medical/pharmaceutical arena.

As you will see from our logo, our primary colors are green and black. We strive to have an efficient, streamlined service offering. I like traditional looks, but also want to showcase our young, modern feel. I would like our card to be double sided.

Target Market(s)

Pharmacies
Hospitals
Physcian Office
Labs

Industry/Entity Type

Business

```html
<!DOCTYPE html>
<html lang="en">
<head>
<meta charset="utf-8">
<title>KLV Courier Business Card</title>
<link rel="stylesheet" href="https://fonts.googleapis.com/css2?family=Questrial&family=Tinos&display=swap">
<style>
  :root {
    --bg: #e4e2dd;
    --card-dark: #1f2221;
    --card-dark-2: #2a2e2c;
    --card-light: #ffffff;
    --green: #2fbf4f;
    --green-deep: #14602a;
    --ink: #1d1f1e;
    --ghost: #2f4236;
    --white: #f4f6f5;
  }
  * { box-sizing: border-box; margin: 0; padding: 0; }
  html, body { width: 1200px; height: 784px; overflow: hidden; }
  body {
    background: var(--bg);
    font-family: "Questrial", "Century Gothic", sans-serif;
    position: relative;
  }
  .card {
    position: absolute;
    top: 237px;
    width: 540px;
    height: 309px;
    border-radius: 4px;
    overflow: hidden;
    box-shadow: 0 6px 18px rgba(0,0,0,0.22);
  }
  .card--back { left: 40px; background: linear-gradient(160deg, var(--card-dark-2), var(--card-dark)); }
  .card--front { left: 620px; background: var(--card-dark); }

  /* back side */
  .back__ghost-name {
    position: absolute;
    left: 0; right: 0; top: 160px;
    text-align: center;
    font-size: 58px;
    letter-spacing: 6px;
    color: var(--ghost);
    line-height: 1;
    white-space: nowrap;
  }
  .back__web {
    position: absolute;
    left: 0; right: 0; top: 108px;
    text-align: center;
    font-size: 27px;
    letter-spacing: 3px;
    color: var(--green);
    white-space: nowrap;
  }

  /* front side */
  .front__shapes { position: absolute; inset: 0; }
  .front__brand {
    position: absolute;
    left: 38px; top: 92px;
    display: flex; align-items: center; gap: 12px;
    color: var(--ink);
    font-size: 40px;
    letter-spacing: 2px;
    line-height: 1;
    white-space: nowrap;
  }
  .front__brand-dot {
    width: 22px; height: 22px;
    border-radius: 50%;
    background: var(--green);
  }
  .front__person {
    position: absolute;
    right: 30px; top: 20px;
    text-align: right;
    line-height: 1.25;
  }
  .front__name { color: var(--green); font-size: 14px; }
  .front__role { color: var(--ink); font-size: 12px; }
  .front__tagline {
    position: absolute;
    left: 16px; top: 199px;
    transform: rotate(-5.8deg);
    transform-origin: left top;
    font-family: "Tinos", "Times New Roman", serif;
    font-size: 13px;
    letter-spacing: 0.4px;
    color: var(--green-deep);
    white-space: nowrap;
  }
  .front__contact {
    position: absolute;
    left: 24px; top: 222px;
    list-style: none;
    color: var(--white);
    font-size: 16px;
    line-height: 19px;
    white-space: nowrap;
  }
  .front__contact li { display: flex; align-items: center; gap: 6px; }
  .front__contact svg { width: 14px; height: 14px; flex: none; }
  .front__contact .indent { padding-left: 20px; }
</style>
</head>
<body>

  <section class="card card--back" aria-label="Card back">
    <div class="back__ghost-name">KLV COURIER</div>
    <div class="back__web">www.KLVcourier.net</div>
  </section>

  <section class="card card--front" aria-label="Card front">
    <svg class="front__shapes" viewBox="0 0 540 309" width="540" height="309" aria-hidden="true">
      <polygon points="0,0 540,0 540,142 0,197" fill="var(--card-light)"/>
      <polygon points="0,197 540,142 540,160 0,215" fill="var(--green)"/>
    </svg>

    <div class="front__brand"><span class="front__brand-dot"></span>KLV COURIER</div>

    <div class="front__person">
      <div class="front__name">Dana Whitlock</div>
      <div class="front__role">Founder</div>
    </div>

    <div class="front__tagline">MOVING MEDICAL DELIVERIES SAFELY ACROSS THE REGION</div>

    <ul class="front__contact">
      <li>
        <svg viewBox="0 0 24 24"><path fill="var(--green)" d="M6.6 10.8a15 15 0 0 0 6.6 6.6l2.2-2.2a1 1 0 0 1 1-.25 11.4 11.4 0 0 0 3.6.6 1 1 0 0 1 1 1V20a1 1 0 0 1-1 1A17 17 0 0 1 3 4a1 1 0 0 1 1-1h3.5a1 1 0 0 1 1 1 11.4 11.4 0 0 0 .6 3.6 1 1 0 0 1-.25 1z"/></svg>
        1555 204 731
      </li>
      <li>
        <svg viewBox="0 0 24 24"><path fill="var(--green)" d="M3 5h18a1 1 0 0 1 1 1v12a1 1 0 0 1-1 1H3a1 1 0 0 1-1-1V6a1 1 0 0 1 1-1zm1 2.2V17h16V7.2l-8 5.3z"/></svg>
        dana@KLVcourier.net
      </li>
      <li>
        <svg viewBox="0 0 24 24"><path fill="var(--green)" d="M12 3l10 9h-3v8h-5v-5h-4v5H5v-8H2z"/></svg>
        4820 Maple Ridge Dr,
      </li>
      <li class="indent">Carmel, IN 46000</li>
    </ul>
  </section>

</body>
</html>
```